Anzeigengestaltung für Bernhardinerzucht
Unkomplizierte Zusammenarbeit, der erste Entwurf hat bis auf kleine Änderungswünsche sofort gefallen.
Zielgruppe
Ich bin neu in der Bernhardinerzucht und möchte auf mich aufmerksam machen. Wir haben Anfang März unseren ersten A - Wurf Bernhardiner bekommen.
Unsere Zielgruppe sind interessierte Käufer der Rasse und andere Züchter.
Aufgabenstellung
Wir haben hübsche Welpen aus der Verpaarung von :
Rüde:
Bruno vom Haldenmoor
Hündin :
Elsa-Mai vom Haldenfeld
Die drei Rüden wurden am 6. März geboren. Sie sind Mitte Mai geimpft, mehrfach entwurmt und gechipt abgabebereit.
Kurze Beschreibung
Wir sind eine kleine Zuchtstätte.
Unser Ziel ist es, mit viel Liebe wesensfeste, gesunde und möglichst langlebige Bernhardiner
zu züchten.
Format DIN A6 ist eine halbe Seite eines Zuchtkatalog für eine Spezialzuchtschau Bernhardiner
Bitte bei den Bildern möglichst nur den Oberkörper/Kopf verwenden. Es sind zwei Bilder der Hündin und ein Bild des Rüden (Bruno vom Haldenmoor) verfügbar.

```html
<!DOCTYPE html>
<html lang="de">
<head>
<meta charset="utf-8">
<title>Bernhardiner-Welpen suchen ein Zuhause</title>
<link href="https://fonts.googleapis.com/css2?family=Bree+Serif&family=Open+Sans:wght@400;600;700&display=swap" rel="stylesheet">
<style>
  :root {
    --orange: #c4772f;
    --charcoal: #3f3936;
    --cream: #f4f1ee;
    --white: #ffffff;
    --ink: #3a3431;
    --soft-white: #e9e4e0;
    --fur-brown: #8c4a2b;
    --fur-dark: #5a3526;
  }
  * { margin: 0; padding: 0; box-sizing: border-box; }
  html, body { width: 1200px; height: 851px; overflow: hidden; background: var(--cream); }
  .ad {
    position: relative; width: 1200px; height: 851px; overflow: hidden;
    background: var(--cream);
    font-family: "Open Sans", Arial, sans-serif;
    color: var(--ink);
  }
  .litter-photo {
    position: absolute; left: 330px; top: 90px; width: 870px; height: 560px;
    background:
      radial-gradient(ellipse 320px 200px at 78% 58%, rgba(240,232,226,0.75), transparent 70%),
      radial-gradient(ellipse 260px 160px at 52% 58%, rgba(110,64,44,0.85), transparent 70%),
      linear-gradient(90deg, var(--cream) 0%, #e7d6cb 18%, #b27a5a 38%, var(--fur-brown) 58%, var(--fur-dark) 78%, #a86a48 100%);
  }
  .puppy-icons {
    position: absolute; left: 905px; top: 12px; width: 250px; height: 68px;
    border-radius: 10px;
    background: linear-gradient(90deg, #e8d8c6, #b98a5e, #e8d8c6);
    opacity: 0.9;
  }
  .shapes { position: absolute; inset: 0; width: 1200px; height: 851px; }
  .headline {
    position: absolute; left: 28px; top: 22px;
    font-family: "Bree Serif", Georgia, serif; font-weight: 400;
    color: var(--white); line-height: 1.12;
  }
  .headline .main { display: block; font-size: 56px; }
  .headline .sub { display: block; font-size: 44px; }
  .litter-badge {
    position: absolute; left: 679px; top: 33px; width: 160px; height: 160px;
    border-radius: 50%; background: var(--charcoal);
    display: flex; align-items: center; justify-content: center; text-align: center;
    font-family: "Bree Serif", Georgia, serif; color: var(--white);
    font-size: 34px; line-height: 1.05;
    transform: rotate(-8deg);
  }
  .facts {
    position: absolute; left: 28px; top: 222px; list-style: none;
    font-family: "Bree Serif", Georgia, serif; font-size: 31px; line-height: 41px;
    color: var(--ink);
  }
  .facts li { padding-left: 22px; text-indent: -22px; }
  .facts li::before { content: "•"; display: inline-block; width: 22px; text-indent: 0; }
  .parent-label {
    position: absolute; border-radius: 50%; background: var(--charcoal);
    border: 5px solid var(--orange);
    display: flex; flex-direction: column; align-items: center; justify-content: center;
    text-align: center; color: var(--white); font-size: 17px; line-height: 1.25;
    z-index: 2;
  }
  .parent-label strong { font-weight: 700; }
  .sire-label { left: 24px; top: 453px; width: 152px; height: 152px; }
  .dam-label { left: 526px; top: 444px; width: 156px; height: 156px; }
  .parent-photo { position: absolute; border-radius: 50%; border: 7px solid var(--orange); z-index: 1; }
  .sire-photo {
    left: 147px; top: 508px; width: 214px; height: 214px;
    background: radial-gradient(circle at 50% 45%, #f2ece8 0%, #a9684a 40%, #5b3325 75%, #e8eef2 100%);
  }
  .dam-photo {
    left: 347px; top: 502px; width: 198px; height: 198px;
    background: radial-gradient(circle at 50% 50%, #f4eee9 0%, #9a5a3c 40%, #5a3a2c 70%, #8fa06a 100%);
  }
  .mission {
    position: absolute; left: 28px; top: 745px; white-space: nowrap;
    color: var(--white); font-weight: 700; font-size: 20px; line-height: 29px;
    letter-spacing: 0.3px;
  }
  .divider {
    position: absolute; left: 624px; top: 673px; width: 3px; height: 157px;
    background: var(--orange);
  }
  .kennel-dot {
    position: absolute; left: 664px; top: 664px; width: 40px; height: 40px;
    border-radius: 50%; background: var(--orange);
  }
  .kennel {
    position: absolute; left: 734px; top: 648px; color: var(--white);
    font-family: "Bree Serif", Georgia, serif;
  }
  .kennel .name { display: block; font-size: 31px; line-height: 40px; }
  .kennel .suffix { display: block; font-size: 22px; line-height: 30px; margin-top: 2px; }
  .contact-address {
    position: absolute; left: 682px; top: 744px; font-style: normal;
    color: var(--soft-white); font-size: 20px; line-height: 29px; letter-spacing: 0.4px;
  }
  .contact-address strong { color: var(--white); font-weight: 700; }
  .contact-phone {
    position: absolute; left: 914px; top: 764px; color: var(--white);
    font-family: "Open Sans", Arial, sans-serif; font-weight: 600; font-size: 29px;
    letter-spacing: 1.5px; line-height: 40px;
    display: flex; align-items: center; gap: 6px;
  }
  .contact-phone svg { width: 30px; height: 30px; }
  .contact-mail {
    position: absolute; left: 920px; top: 802px; color: var(--soft-white);
    font-size: 20.5px; letter-spacing: 0.4px; line-height: 29px;
  }
</style>
</head>
<body>
<main class="ad">
  <div class="litter-photo" role="img" aria-label="Foto: Bernhardiner-Hündin liegt mit ihren drei Welpen, die bei ihr trinken"></div>

  <svg class="shapes" viewBox="0 0 1200 851" aria-hidden="true">
    <defs>
      <linearGradient id="photoFade" x1="0" x2="1">
        <stop offset="0" stop-color="#f4f1ee" stop-opacity="1"/>
        <stop offset="0.22" stop-color="#f4f1ee" stop-opacity="0.85"/>
        <stop offset="0.45" stop-color="#f4f1ee" stop-opacity="0"/>
      </linearGradient>
    </defs>
    <rect x="0" y="90" width="900" height="560" fill="url(#photoFade)"/>
    <path class="top-band" d="M0 0 H1200 V70 C 950 82, 700 120, 0 178 Z" fill="#c4772f"/>
    <path class="top-swoosh" d="M520 176 C 760 132, 980 96, 1200 75 V103 C 980 112, 760 142, 520 176 Z" fill="#3f3936"/>
    <path class="bottom-stripe" d="M0 624 C 380 610, 800 596, 1200 582 V640 H0 Z" fill="#c4772f"/>
    <path class="bottom-band" d="M0 645 C 380 632, 800 618, 1200 604 V851 H0 Z" fill="#3f3936"/>
  </svg>

  <div class="puppy-icons" role="img" aria-label="Illustration: drei gezeichnete Bernhardiner-Welpenköpfe"></div>

  <h1 class="headline">
    <span class="main">Bernhardiner-Welpen</span>
    <span class="sub">suchen ein Zuhause</span>
  </h1>

  <div class="litter-badge">unser<br>A-Wurf</div>

  <ul class="facts">
    <li>drei Rüden</li>
    <li>geboren am 6. März 2019</li>
    <li>Abgabe Mitte Mai</li>
    <li>geimpf, entwurmt<br>und gechipt</li>
  </ul>

  <div class="parent-photo sire-photo" role="img" aria-label="Foto: Rüde Bruno vom Haldenmoor im Schnee, Oberkörper und Kopf"></div>
  <div class="parent-photo dam-photo" role="img" aria-label="Foto: Hündin Elsa-Mai vom Haldenfeld vor einem Haus, Oberkörper und Kopf"></div>

  <div class="parent-label sire-label">
    <span>Rüde:</span>
    <strong>Bruno vom<br>Haldenmoor</strong>
    <span>(langhaar)</span>
  </div>
  <div class="parent-label dam-label">
    <span>Hündin:</span>
    <strong>Elsa-Mai vom<br>Haldenfeld</strong>
    <span>(langhaar)</span>
  </div>

  <p class="mission">Wir sind eine kleine Zucht. Unser Ziel ist es,<br>mit viel Liebe wesensfeste gesunde und<br>möglichst langlebige Bernhardiner zu züchten.</p>

  <div class="divider"></div>

  <div class="kennel-dot" aria-hidden="true"></div>
  <div class="kennel">
    <span class="name">St. Bernhards-Zuchtstätte</span>
    <span class="suffix">vom oberen Talgrund</span>
  </div>

  <address class="contact-address">
    <strong>Merle Soltau</strong><br>
    Lindenweg 14<br>
    36199 Talbrunn
  </address>

  <div class="contact-phone">
    <svg viewBox="0 0 24 24" aria-hidden="true"><path d="M6.6 10.8c1.4 2.8 3.8 5.1 6.6 6.6l2.2-2.2c.3-.3.7-.4 1-.2 1.1.4 2.3.6 3.6.6.6 0 1 .4 1 1V20c0 .6-.4 1-1 1C10.6 21 3 13.4 3 4c0-.6.4-1 1-1h3.5c.6 0 1 .4 1 1 0 1.3.2 2.5.6 3.6.1.3 0 .7-.2 1z" fill="none" stroke="#ffffff" stroke-width="1.6"/></svg>
    <span>0170/5558231</span>
  </div>
  <div class="contact-mail">merle.soltau@mailpost.de</div>
</main>
</body>
</html>
```